Brochure AESTHETIC MEDICINE
NOEMI VALDEZ MEDICINA ESTETICA ESPECIALIZADA
Project: Brochure AESTHETIC MEDICINE
Brochure AESTHETIC MEDICINE - Health
Creative Brief
Health
PEOPLE WHO WANT TO BE YOUNGER, BETTER PHYSICALLY AND REJUVENATED. MEN AND WOMEN WHO WANT TO SHAPE YOUR BODY AND HAVE A BETTER FIGURE
Brochure will be tri-fold. Content details attached.

```html
<!DOCTYPE html>
<html lang="es">
<head>
<meta charset="utf-8">
<title>Noemi Valdez — Medicina Estética Especializada · Tríptico</title>
<link href="https://fonts.googleapis.com/css2?family=Montserrat:wght@400;600;700&family=Crimson+Text:ital@0;1&display=swap" rel="stylesheet">
<style>
  :root{
    --purple:#6a2c8c;
    --purple-light:#8c52b3;
    --purple-pale:#efe6f5;
    --silver:#c9c9cf;
    --silver-light:#ececf0;
    --ink:#4a4a50;
    --ink-soft:#7b7b82;
    --paper:#ffffff;
    --backdrop:#e4e4e8;
  }
  *{box-sizing:border-box;margin:0;padding:0}
  html,body{width:1200px;height:961px;overflow:hidden}
  body{background:var(--backdrop);font-family:"Montserrat",Arial,sans-serif;color:var(--ink);position:relative}
  .spread{position:absolute;left:40px;width:1120px;height:430px;background:var(--paper);display:grid;grid-template-columns:repeat(3,1fr);box-shadow:0 4px 14px rgba(0,0,0,.18);overflow:hidden}
  .spread--outside{top:30px}
  .spread--inside{top:501px}
  .panel{position:relative;padding:22px 24px;border-right:1px solid #f0f0f2}
  .panel:last-child{border-right:none}
  .swoosh{position:absolute;left:0;bottom:0;width:100%;height:110px;pointer-events:none}

  /* brand */
  .brand{display:flex;flex-direction:column;align-items:center;gap:4px;position:relative;z-index:2}
  .brand__dot{width:34px;height:34px;border-radius:50%;background:var(--purple)}
  .brand__name{font-weight:600;font-size:17px;letter-spacing:3px;color:var(--purple)}
  .brand__tag{font-size:6.5px;letter-spacing:1.5px;color:var(--ink-soft)}

  /* photo placeholders */
  .photo{background:radial-gradient(circle at 40% 40%,#f4e1d6,#d8b8a8 70%,#bfa096);}
  .photo--round{border-radius:50%;border:4px solid var(--silver-light);box-shadow:0 0 0 2px var(--silver)}
  .map{background:linear-gradient(135deg,#eeeeee,#d9d9d9);border:1px solid #ccc}

  /* text blocks */
  .feature{display:grid;grid-template-columns:76px 1fr;gap:12px;margin-bottom:22px}
  .feature .photo{width:76px;height:76px}
  .feature__title{font-size:9px;font-weight:700;color:var(--purple);letter-spacing:1px;margin-bottom:4px}
  .copy{font-size:8.5px;line-height:1.45;color:var(--ink-soft)}

  .contact{font-size:9px;line-height:1.7;color:var(--ink);margin-top:14px}
  .contact__row{display:flex;align-items:center;gap:6px}
  .contact__row svg{width:10px;height:10px;fill:var(--purple)}
  .dots{display:flex;gap:6px;justify-content:center;margin-top:12px}
  .dots span{width:16px;height:16px;border-radius:50%;background:var(--purple)}

  /* cover */
  .cover{padding:22px 0 0}
  .cover__photo{position:absolute;left:40px;top:96px;width:292px;height:172px;border-radius:0 0 120px 0;background:linear-gradient(160deg,#f6e7dd,#dcbcac 60%,#c59f90);z-index:1}
  .cover__band{position:absolute;left:0;bottom:0;width:100%;height:150px;z-index:2}
  .cover__slogan{position:absolute;right:26px;bottom:46px;font-family:"Crimson Text",Georgia,serif;font-size:36px;line-height:1;color:#fff;text-align:left;z-index:3}
  .cover__web{position:absolute;right:26px;bottom:20px;font-size:9px;color:#fff;letter-spacing:.5px;z-index:3}

  /* inside */
  .about__photo{width:150px;height:150px;margin:0 auto 14px;display:block}
  .about__title{font-size:12px;font-weight:700;color:var(--purple)}
  .about__sub{font-size:8px;color:var(--ink-soft);margin-bottom:8px}
  .about__thumbs{position:absolute;left:30px;bottom:16px;display:flex;gap:10px;z-index:2}
  .about__thumbs .photo{width:54px;height:54px}

  .list-block{margin-bottom:9px}
  .list-block__head{background:var(--purple);color:#fff;font-size:8.5px;font-weight:700;letter-spacing:1px;padding:4px 8px;margin-bottom:4px}
  .list{list-style:none;font-size:8.5px;line-height:1.38;color:var(--ink);columns:2;column-gap:10px}
  .list li::before{content:"";display:inline-block;width:5px;height:5px;border-radius:50%;background:var(--purple-light);margin-right:5px;vertical-align:1px}
  .list--single{columns:1}

  .surgery{display:grid;grid-template-columns:1fr 96px;gap:10px}
  .surgery__photos{display:flex;flex-direction:column;gap:10px}
  .surgery__photos .photo{width:92px;height:92px}
  .products{position:absolute;left:0;bottom:0;width:100%;height:86px;background:var(--purple);color:#fff;padding:14px 24px 0 120px;z-index:2}
  .products__title{font-size:12px;font-weight:700;letter-spacing:1.5px;margin-bottom:4px}
  .products__copy{font-size:8px;line-height:1.4}
  .products__photo{position:absolute;left:22px;top:-22px;width:84px;height:84px}
</style>
</head>
<body>

<!-- OUTSIDE -->
<section class="spread spread--outside">
  <div class="panel">
    <div class="feature">
      <div class="photo photo--round" role="img" aria-label="Retrato de la doctora en consulta"></div>
      <div>
        <h3 class="feature__title">NOEMI VALDEZ</h3>
        <p class="copy">Médica especialista en medicina estética con amplia experiencia en tratamientos faciales y corporales. Su enfoque combina técnicas modernas con atención cercana, buscando resultados naturales y seguros para cada paciente que desea sentirse renovado.</p>
      </div>
    </div>
    <div class="feature">
      <div class="photo photo--round" role="img" aria-label="Tratamiento facial con microcorriente"></div>
      <div>
        <h3 class="feature__title">MICROCORRIENTE FACIAL</h3>
        <p class="copy">Tecnología suave que estimula los músculos del rostro, mejora la firmeza y la luminosidad de la piel. Sesiones cómodas, sin dolor y sin tiempo de recuperación, ideales para mantener un aspecto fresco.</p>
      </div>
    </div>
    <svg class="swoosh" viewBox="0 0 373 110" preserveAspectRatio="none" aria-hidden="true">
      <path d="M0 70 Q190 30 373 60 L373 110 L0 110Z" fill="var(--silver-light)"/>
      <path d="M0 88 Q190 50 373 80 L373 110 L0 110Z" fill="var(--purple)"/>
    </svg>
  </div>

  <div class="panel">
    <div class="brand">
      <span class="brand__dot"></span>
      <span class="brand__name">NOEMI VALDEZ</span>
      <span class="brand__tag">MEDICINA ESTÉTICA ESPECIALIZADA</span>
    </div>
    <div class="map" role="img" aria-label="Mapa de ubicación del consultorio" style="height:130px;margin-top:18px"></div>
    <div class="dots"><span></span><span></span><span></span></div>
    <div class="contact">
      <div class="contact__row"><svg viewBox="0 0 10 10"><path d="M5 0a3.5 3.5 0 0 0-3.5 3.5C1.5 6 5 10 5 10s3.5-4 3.5-6.5A3.5 3.5 0 0 0 5 0zm0 5a1.5 1.5 0 1 1 0-3 1.5 1.5 0 0 1 0 3z"/></svg>Calle Almendros 214, Consultorio 3</div>
      <div class="contact__row"><svg viewBox="0 0 10 10"><path d="M2 0h2l1 2.5-1.3 1a6 6 0 0 0 2.8 2.8l1-1.3L10 6v2c0 1-1 2-2 2A8 8 0 0 1 0 2c0-1 1-2 2-2z"/></svg>(55) 4120 7788</div>
      <div class="contact__row"><svg viewBox="0 0 10 10"><path d="M0 2h10v6H0zm0 0l5 3.5L10 2" fill="none" stroke="var(--purple)" stroke-width="1"/></svg>citas@noemivaldezestetica.com</div>
      <div class="contact__row"><svg viewBox="0 0 10 10"><circle cx="5" cy="5" r="4.3" fill="none" stroke="var(--purple)" stroke-width="1.2"/></svg>www.noemivaldezestetica.com</div>
    </div>
    <svg class="swoosh" viewBox="0 0 373 110" preserveAspectRatio="none" aria-hidden="true">
      <path d="M0 60 Q190 90 373 50 L373 110 L0 110Z" fill="var(--silver-light)"/>
    </svg>
  </div>

  <div class="panel cover">
    <div class="brand">
      <span class="brand__dot"></span>
      <span class="brand__name">NOEMI VALDEZ</span>
      <span class="brand__tag">MEDICINA ESTÉTICA ESPECIALIZADA</span>
    </div>
    <div class="cover__photo" role="img" aria-label="Fotografía de una mujer con piel radiante tocando su rostro"></div>
    <svg class="cover__band" viewBox="0 0 373 150" preserveAspectRatio="none" aria-hidden="true">
      <path d="M0 22 Q180 40 373 0 L373 150 L0 150Z" fill="var(--silver)"/>
      <path d="M0 38 Q180 56 373 16 L373 150 L0 150Z" fill="var(--purple)"/>
    </svg>
    <p class="cover__slogan">Reinvent<br>yourself...</p>
    <p class="cover__web">www.noemivaldezestetica.com</p>
  </div>
</section>

<!-- INSIDE -->
<section class="spread spread--inside">
  <div class="panel">
    <div class="photo photo--round about__photo" role="img" aria-label="Procedimiento estético facial con aplicación en la piel"></div>
    <h2 class="about__title">ABOUT Noemi Valdez</h2>
    <p class="about__sub">Medicina Estética Especializada</p>
    <p class="copy">Nuestra consulta ofrece tratamientos personalizados para hombres y mujeres que desean verse más jóvenes y sentirse mejor. Cada plan se diseña tras una valoración médica completa, con tecnología actual y protocolos seguros que respetan tu bienestar.</p>
    <div class="about__thumbs">
      <div class="photo photo--round" role="img" aria-label="Tratamiento corporal"></div>
      <div class="photo photo--round" role="img" aria-label="Cuidado de la piel"></div>
    </div>
    <svg class="swoosh" viewBox="0 0 373 110" preserveAspectRatio="none" aria-hidden="true">
      <path d="M0 50 Q190 20 373 60 L373 110 L0 110Z" fill="var(--silver-light)"/>
      <path d="M0 74 Q190 44 373 84 L373 110 L0 110Z" fill="var(--purple)"/>
    </svg>
  </div>

  <div class="panel">
    <div class="list-block">
      <h3 class="list-block__head">REJUVENECIMIENTO FACIAL</h3>
      <ul class="list"><li>Toxina botulínica</li><li>Ácido hialurónico</li><li>Peeling químico</li><li>Mesoterapia facial</li><li>Radiofrecuencia</li><li>Hilos tensores</li><li>Plasma rico</li><li>Microcorriente</li></ul>
    </div>
    <div class="list-block">
      <h3 class="list-block__head">REJUVENECIMIENTO CORPORAL</h3>
      <ul class="list"><li>Carboxiterapia</li><li>Drenaje linfático</li><li>Cavitación</li><li>Lipólisis láser</li><li>Mesoterapia corporal</li><li>Moldeo corporal</li></ul>
    </div>
    <div class="list-block">
      <h3 class="list-block__head">TÉCNICAS ANTIENVEJECIMIENTO</h3>
      <ul class="list"><li>Sueroterapia</li><li>Terapia hormonal</li><li>Nutrición celular</li><li>Antioxidantes</li></ul>
    </div>
    <div class="list-block">
      <h3 class="list-block__head">TERAPIAS ESPECIALES</h3>
      <ul class="list"><li>Manchas y acné</li><li>Cicatrices</li><li>Caída del cabello</li><li>Várices finas</li></ul>
    </div>
  </div>

  <div class="panel">
    <div class="list-block">
      <h3 class="list-block__head">CIRUGÍA PLÁSTICA</h3>
    </div>
    <div class="surgery">
      <ul class="list list--single"><li>Rinoplastia</li><li>Blefaroplastia</li><li>Lifting facial</li><li>Mamoplastia</li><li>Abdominoplastia</li><li>Liposucción</li><li>Lipoescultura</li><li>Otoplastia</li><li>Mentoplastia</li><li>Gluteoplastia</li><li>Bichectomía</li><li>Valoración previa</li></ul>
      <div class="surgery__photos">
        <div class="photo photo--round" role="img" aria-label="Paciente tras tratamiento de rejuvenecimiento"></div>
        <div class="photo photo--round" role="img" aria-label="Valoración médica de cirugía plástica"></div>
      </div>
    </div>
    <div class="products">
      <div class="photo photo--round products__photo" role="img" aria-label="Productos dermocosméticos"></div>
      <h3 class="products__title">PRODUCTOS</h3>
      <p class="products__copy">Línea dermocosmética profesional para el cuidado diario de la piel, recomendada según tu tipo y tratamiento.</p>
    </div>
  </div>
</section>

</body>
</html>
```